Attorney company looking for 2 full page magazine ads

We need 2 magazine ads for a homeowner association law firm in Houston, called Brandt & Pell, P.C. Our tagline is "Results and Responsiveness", so we would like for our ads to have a "high risk" theme. I've included examples of our previous ads that we used in the past, so you can see what I mean by a "high risk" theme. Also included is our firm logo, and tagline. The size of each ad will need to be 8.625 11.125 (w/ bleed) or 8 x 10.5 (without bleed).

Target Market(s)

Homeowners Associations and management companies

Industry/Entity Type

Legal

Requirements
Must have
• Logo, tagline- Results and Responsiveness. High risk theme.
Nice to have
• Professional design, clean design that gets the point across.
Should not have
• Clip art, copyright images

```html
<!DOCTYPE html>
<html lang="en">
<head>
<meta charset="utf-8">
<title>Brandt &amp; Pell, P.C. – Magazine Ad</title>
<link rel="stylesheet" href="https://fonts.googleapis.com/css2?family=Kalam:wght@700&family=Roboto:wght@400;500;700;900&family=Libre+Baskerville:wght@700&display=swap">
<style>
  :root {
    --backdrop: #8a93a3;
    --paper: #ffffff;
    --navy: #2e3d7a;
    --royal: #2f49a8;
    --sky: #2a8fd6;
    --red: #d4141c;
    --gold: #a98a4e;
    --ink: #222a3a;
    --muted: #444b58;
    --art-warm: #e7c9a6;
    --art-brown: #d9b79a;
    --art-grey: #e3e3e7;
    --art-teal: #c6dbe6;
  }
  * { margin: 0; padding: 0; box-sizing: border-box; }
  html, body {
    width: 1200px; height: 620px; overflow: hidden;
    background: var(--backdrop);
  }
  .ad-page {
    position: absolute;
    left: 370px; top: 13px;
    width: 460px; height: 594px;
    background: var(--paper);
    box-shadow: 0 4px 14px rgba(0,0,0,.25);
    font-family: "Roboto", Arial, sans-serif;
  }
  .tagline-banner {
    position: absolute;
    left: 63px; top: 37px;
    width: 334px; height: 28px;
    border-radius: 14px;
    background: linear-gradient(90deg, var(--navy) 0%, #2b5aa8 60%, var(--sky) 100%);
    color: #fff;
    font-size: 23px;
    font-weight: 400;
    line-height: 28px;
    text-align: center;
    letter-spacing: .2px;
  }
  .headline {
    position: absolute;
    left: 0; top: 92px;
    width: 460px;
    text-align: center;
    font-family: "Kalam", "Comic Sans MS", cursive;
    font-weight: 700;
    font-size: 36px;
    line-height: 42px;
    color: var(--royal);
  }
  .headline .accent { color: var(--red); }
  .hero-art {
    position: absolute;
    left: 38px; top: 196px;
    width: 384px; height: 310px;
  }
  .footer {
    position: absolute;
    left: 22px; top: 524px;
    width: 420px;
  }
  .firm-name {
    position: absolute;
    left: 0; top: 10px;
    width: 135px;
    text-align: center;
    font-family: "Libre Baskerville", Georgia, serif;
    font-weight: 700;
    font-size: 13px;
    color: var(--gold);
  }
  .phone {
    position: absolute;
    left: 146px; top: 0;
    display: flex; align-items: center; gap: 4px;
    font-size: 20px; font-weight: 700;
    color: var(--royal);
  }
  .contact-list {
    position: absolute;
    left: 297px; top: 0;
    list-style: none;
    font-size: 8px;
    line-height: 11px;
    color: var(--ink);
  }
  .contact-list li { display: flex; align-items: center; gap: 3px; }
  .disclaimer {
    position: absolute;
    left: 140px; top: 28px;
    width: 280px;
    text-align: center;
    font-size: 5.6px;
    line-height: 7.6px;
    color: var(--muted);
  }
</style>
</head>
<body>
  <main class="ad-page">
    <div class="tagline-banner">Results &amp; Responsiveness</div>

    <h1 class="headline">When results are<br><span class="accent">critical</span> to your future</h1>

    <svg class="hero-art" viewBox="0 0 384 310" role="img"
         aria-label="Illustration of the high risk theme: an archer in medieval costume draws a bow at a worried man in a blue jacket with an apple on his head, pierced by an arrow, before a faint grey city silhouette">
      <defs>
        <linearGradient id="artTones" x1="0" y1="0" x2="1" y2="0">
          <stop offset="0" stop-color="var(--art-warm)"/>
          <stop offset=".3" stop-color="var(--art-brown)"/>
          <stop offset=".55" stop-color="var(--art-grey)"/>
          <stop offset="1" stop-color="var(--art-teal)"/>
        </linearGradient>
        <radialGradient id="artFade" cx=".5" cy=".55" r=".6">
          <stop offset="0" stop-color="#fff" stop-opacity="1"/>
          <stop offset=".7" stop-color="#fff" stop-opacity=".7"/>
          <stop offset="1" stop-color="#fff" stop-opacity="0"/>
        </radialGradient>
        <mask id="artMask">
          <rect width="384" height="310" fill="url(#artFade)"/>
        </mask>
      </defs>
      <rect width="384" height="310" fill="url(#artTones)" mask="url(#artMask)"/>
    </svg>

    <footer class="footer">
      <div class="firm-name">Brandt &amp; Pell, P.C.</div>

      <div class="phone">
        <svg width="13" height="13" viewBox="0 0 16 16" aria-hidden="true">
          <circle cx="8" cy="8" r="7" fill="none" stroke="var(--gold)" stroke-width="1.6"/>
          <path d="M5.6 4.6l1.3 1.6-.7 1c.5 1 1.2 1.7 2.2 2.2l1-.7 1.6 1.3-.8 1.2C7.8 11.2 4.9 8.3 4.6 5.8z" fill="var(--gold)"/>
        </svg>
        713-555-0148
      </div>

      <ul class="contact-list">
        <li>
          <svg width="6" height="6" viewBox="0 0 10 10" aria-hidden="true"><circle cx="5" cy="5" r="4.2" fill="none" stroke="var(--gold)" stroke-width="1"/><path d="M1 5h8M5 1v8" stroke="var(--gold)" stroke-width=".8"/></svg>
          www.brandtpell.com
        </li>
        <li>
          <svg width="6" height="6" viewBox="0 0 10 10" aria-hidden="true"><rect x="1" y="2" width="8" height="6" fill="none" stroke="var(--gold)" stroke-width="1"/><path d="M1 2l4 3.5L9 2" fill="none" stroke="var(--gold)" stroke-width=".8"/></svg>
          information@brandtpell.com
        </li>
      </ul>

      <p class="disclaimer">Daniel R. Brandt is Board certified in Residential and Commercial Real Estate Law by the State Board of Legal Certification. Otherwise, Not Certified by the State Board of Legal Certification.</p>
    </footer>
  </main>
</body>
</html>
```